Book and Ebook Cover for my Upcoming Book

About the Book
------------------
I need a book, ebook and if possible audio cover design for my upcoming book - Lanterns & Larkspur. This is my first book and really looking for a great book cover. The book is about my story, living with Mental Health and how to reclaim control of your life.

Quillbarrow
-----------
I am using quillbarrow.com to self-publish my book so in case of any design-related questions you can just search info on their website.

I have an initial theme I am thinking for the design book cover which I have attached. You can use this as a starting point.

Idea for the theme
---------------------
I am thinking about a phoenix to represent rising from the ashes and rebirth. The phoenix motif will be continued throughout the interior pages of the book. I'd like the cover of the book to be minimal, white with gold lettering, and maybe incorporating wings? feel free to play around with the idea and up for suggestions.

If you can think of something along these lines and make it a lot better that would be great.

What I need
---------------
The book is complete and is Trim size is 6.14 x 9.21” (234 x 156mm). I would need-
1. Book Cover
2. Back & Spine Design
3. Source File
4. Ebook Cover
5. Need multiple revisions to get the best possible outcome
6. My name and book title should also on the front cover
7. The book title should be bigger size than the subtitle

If you can give me Audiobook cover, I would love that as well and can pay extra for it if needed.

I love this for the interior phoenix motif:
https://craftbazaarly.com/InkMoth/7720458-Watercolor-Heron-Clipart-Set#fullscreen

The only other actual book cover I found online that remotely relates to what I am looking for is this -
https://www.lookfinder.example/url?sa=i&url=https%3A%2F%2Fpixelmoor.com%2Fvantrell&psig=QxTrPLm3KZ9vBwE2dYcN41HoJuSA&ust=1598415525610000&source=images&cd=vfe&ved=0CAIQjRxqFwoTCPD_toPAtesCFQAAAAAdAAAAABAD

Target Market(s)

Personal Development
Mental health

Requirements
Must have
• 1. Book Cover
2. Back & Spine Design
3. Source File
4. Ebook Cover
Nice to have
• Audiobook cover as I eventually will be releasing the audio version of the book

```html
<!DOCTYPE html>
<html lang="en">
<head>
<meta charset="utf-8">
<title>Lanterns &amp; Larkspur — Front Cover</title>
<link rel="stylesheet" href="https://fonts.googleapis.com/css2?family=Cinzel:wght@400;500;600&display=swap">
<style>
  :root {
    --paper: #ffffff;
    --paper-shade: #ececec;
    --gold-dark: #6e5420;
    --gold-mid: #b08a3e;
    --gold-light: #e3c27a;
    --ink-grey: #4a4a4a;
    --rule-grey: #8a8a8a;
  }
  * { margin: 0; padding: 0; box-sizing: border-box; }
  html, body {
    width: 886px;
    height: 1200px;
    overflow: hidden;
  }
  body {
    background: var(--paper);
    font-family: "Cinzel", serif;
  }
  .cover {
    position: relative;
    width: 886px;
    height: 1200px;
    background: linear-gradient(100deg, var(--paper) 0%, var(--paper) 55%, var(--paper-shade) 100%);
    text-align: center;
  }
  .gold-text {
    background: linear-gradient(90deg, var(--gold-dark) 0%, var(--gold-mid) 30%, var(--gold-light) 55%, var(--gold-mid) 75%, var(--gold-dark) 100%);
    -webkit-background-clip: text;
    background-clip: text;
    color: transparent;
  }
  .title-line {
    position: absolute;
    left: 0;
    width: 100%;
    font-weight: 600;
    font-size: 92px;
    line-height: 1;
    letter-spacing: 1px;
  }
  .title-line .cap { font-size: 112px; }
  .title-line--first { top: 110px; }
  .title-line--second { top: 298px; }
  .title-divider {
    position: absolute;
    top: 232px;
    left: 90px;
    width: 706px;
    display: flex;
    align-items: center;
    gap: 26px;
  }
  .title-divider .rule {
    flex: 1;
    height: 2px;
    background: linear-gradient(90deg, transparent, var(--gold-mid), var(--gold-dark));
  }
  .title-divider .rule--right {
    background: linear-gradient(90deg, var(--gold-dark), var(--gold-mid), transparent);
  }
  .title-divider .ampersand {
    font-family: "Cinzel", serif;
    font-size: 54px;
    color: var(--rule-grey);
    line-height: 1;
  }
  .phoenix-emblem {
    position: absolute;
    top: 470px;
    left: 100px;
    width: 690px;
    height: 420px;
    border-radius: 50% 50% 45% 45%;
    background: radial-gradient(ellipse at 50% 45%, var(--gold-light) 0%, var(--gold-mid) 40%, rgba(176,138,62,0.35) 70%, rgba(255,255,255,0) 100%);
  }
  .subtitle {
    position: absolute;
    top: 930px;
    left: 0;
    width: 100%;
    font-size: 30px;
    line-height: 1.25;
    color: var(--ink-grey);
    letter-spacing: 1px;
  }
  .author {
    position: absolute;
    top: 1052px;
    left: 0;
    width: 100%;
    font-size: 66px;
    font-weight: 600;
    line-height: 1;
    letter-spacing: 2px;
  }
</style>
</head>
<body>
  <main class="cover">
    <h1 class="book-title">
      <span class="title-line title-line--first gold-text"><span class="cap">L</span>ANTERNS</span>
      <span class="title-divider" aria-hidden="true">
        <span class="rule"></span>
        <span class="ampersand">&amp;</span>
        <span class="rule rule--right"></span>
      </span>
      <span class="title-line title-line--second gold-text"><span class="cap">L</span>ARKSPUR</span>
    </h1>
    <div class="phoenix-emblem" role="img" aria-label="Gold phoenix emblem with outstretched wings rising from flames"></div>
    <p class="subtitle">HOW TO RECLAIM<br>CONTROL OF YOUR LIFE</p>
    <p class="author gold-text">VESHNA ROLT</p>
  </main>
</body>
</html>
```